Luxury Wine Label for New Startup Winery

We need a wine label for our new winery startup. We have worked with a local designer but do not feel the resulting label / logo have the elevation required to present our brand as a luxury wine. Our winery is called "Harrowgate Vineyards" and we are focused on extremely high quality hand crafted artisan and estate wines from the Pacific Northwest.
We would like to see designs that utilize a tree line, or other imagery that represents the "Harrowgate" part of our company name. Another interesting feature could be wood grain.
A logo will be required based on your design so please design with this in mind:
This logo should be consistent with the wine bottle label design, and should be representative of our high end exclusive wine while giving a sense of place (Oregon/ Pacific Northwest.)
I will supply an image of the design we received from our local designer, PLEASE NOTE: in general we do like wood grain and tree line concepts but feel the execution was poorly done.
ATTN: Logo design should be suitable for use on: Bottles (Red wine/rose/white wine), Bussiness cards, vehicle signage, business signage, etc
P.S.:
If you have a design that is not outside the box we are still interested in seeing it.
Label is for a burgundy style bottle with a label height of 3.5 - 4" and a width of 3.5-4"
any label <= 4"x4" and >=3.5"x3.5" will be acceptable:
HOWEVER Width should be greater than or equal to height due to the bottle format
Target Market(s)
Wine enthusiasts with adequate discretionary budgets to afford $100 bottles of wine.
Industry/Entity Type
Wine / Winery
Requirements
Must have
- A sense of luxury, a feel of exclusivity, and a theme consistent with our product and brand name
Nice to have
- Tree line, wood grain or other wood themes. Serif fonts
Should not have
- anything cheesy, off topic, hard to read script fonts or anything that makes the label hard to read from a few feet away or too busy

```html
<!DOCTYPE html>
<html lang="en">
<head>
<meta charset="utf-8">
<title>Harrowgate Vineyards — 2024 Pinot Noir Label</title>
<link rel="stylesheet" href="https://fonts.googleapis.com/css2?family=Cormorant+Garamond:wght@500;600&display=swap">
<style>
  :root {
    --page: #ffffff;
    --label-ink: #2a2e38;
    --label-ink-deep: #21242c;
    --gold-soft: rgba(227, 166, 58, 0.14);
    --cream: #f4f1ea;
  }
  html, body {
    margin: 0;
    padding: 0;
    width: 1200px;
    height: 1200px;
    overflow: hidden;
    background: var(--page);
  }
  .canvas {
    position: relative;
    width: 1200px;
    height: 1200px;
    display: flex;
    align-items: center;
    justify-content: center;
  }
  .wine-label {
    position: relative;
    width: 1040px;
    height: 1040px;
    overflow: hidden;
    color: var(--cream);
  }
  .label-backdrop {
    position: absolute;
    inset: 0;
    background:
      radial-gradient(ellipse at 30% 25%, var(--gold-soft), transparent 60%),
      radial-gradient(ellipse at 75% 70%, var(--gold-soft), transparent 55%),
      linear-gradient(160deg, var(--label-ink) 0%, var(--label-ink-deep) 100%);
  }
  .winery-name {
    position: absolute;
    top: 170px;
    left: 0;
    right: 0;
    margin: 0;
    text-align: center;
    font-family: "Cormorant Garamond", Georgia, serif;
    font-weight: 500;
    font-size: 92px;
    line-height: 1;
    letter-spacing: 1px;
    color: var(--cream);
    white-space: nowrap;
  }
  .vintage {
    position: absolute;
    top: 532px;
    left: 0;
    right: 0;
    margin: 0;
    text-align: center;
    font-family: "Cormorant Garamond", Georgia, serif;
    font-weight: 500;
    font-size: 66px;
    line-height: 1;
  }
  .varietal {
    position: absolute;
    top: 600px;
    left: 0;
    right: 0;
    margin: 0;
    text-align: center;
    font-family: "Cormorant Garamond", Georgia, serif;
    font-weight: 600;
    font-size: 150px;
    line-height: 1;
    letter-spacing: 2px;
  }
  .label-footer {
    position: absolute;
    left: 52px;
    right: 52px;
    bottom: 40px;
    display: flex;
    justify-content: space-between;
    font-family: "Cormorant Garamond", Georgia, serif;
    font-weight: 500;
    font-size: 46px;
    line-height: 1;
  }
</style>
</head>
<body>
  <main class="canvas">
    <section class="wine-label">
      <div class="label-backdrop" role="img" aria-label="Dark charcoal background with flowing gold lines and scattered gold speckles"></div>
      <h1 class="winery-name">Harrowgate Vineyards</h1>
      <p class="vintage">2024</p>
      <h2 class="varietal">Pinot Noir</h2>
      <footer class="label-footer">
        <span class="appellation">Willamette Valley, Oregon</span>
        <span class="alcohol">14.2% by Vol.</span>
      </footer>
    </section>
  </main>
</body>
</html>
```